Billboard design 8x3M NURA (Spanish company)

We´re located in the south of Spain. We run a local telecom company.
We sell Fiber optic, and mobile phone lines mainly.
The billboard will have to be in Spanish, I would like the price to be something you spot on first sight when passing by in the car.
Our company color is blue, like in our logo which I will add. I will also add a example from what we currently have.
The new offer should be:
1000 megas + 100Gigas movil con llamadas ilimitadas. (meaning 1000Mb fiber optic speed and 100Gb data and unlimited calls for 1 mobile line)
Our details are: phone line 952 00 0147
Website: nu-ra.es

```html
<!DOCTYPE html>
<html lang="es">
<head>
<meta charset="utf-8">
<title>NURA – Valla 8x3 Fibra + Móvil</title>
<link href="https://fonts.googleapis.com/css2?family=Montserrat:wght@500;600;700;800;900&display=swap" rel="stylesheet">
<style>
  :root {
    --page-bg: #e4e4e4;
    --navy-deep: #0d1a66;
    --navy: #12278a;
    --blue-bright: #1f5bd6;
    --blue-glow: #3d86f0;
    --yellow: #ffd800;
    --white: #ffffff;
  }
  * { margin: 0; padding: 0; box-sizing: border-box; }
  html, body {
    width: 1200px; height: 600px; overflow: hidden;
    background: var(--page-bg);
    font-family: "Montserrat", sans-serif;
  }
  .billboard {
    position: absolute; left: 0; top: 75px;
    width: 1200px; height: 450px;
    background: linear-gradient(90deg, var(--navy-deep) 0%, var(--navy-deep) 40%, var(--navy) 62%, var(--blue-bright) 100%);
    overflow: hidden;
    color: var(--white);
  }
  .hero-art {
    position: absolute; left: 470px; top: 0; width: 730px; height: 450px;
    background:
      radial-gradient(ellipse 180px 150px at 490px 195px, rgba(255,255,255,0.55), transparent 70%),
      radial-gradient(ellipse 150px 220px at 650px 230px, rgba(61,134,240,0.75), transparent 70%),
      linear-gradient(160deg, transparent 40%, rgba(255,216,0,0.22) 55%, rgba(61,134,240,0.35) 65%, transparent 80%);
  }
  .brand {
    position: absolute; left: 57px; top: 38px;
    display: flex; align-items: center; gap: 14px;
  }
  .brand-dot {
    width: 46px; height: 46px; border-radius: 50%;
    background: var(--white);
  }
  .brand-name {
    font-weight: 800; font-size: 72px; letter-spacing: 4px; line-height: 1;
    color: var(--white);
  }
  .services {
    position: absolute; left: 57px; top: 122px; width: 280px;
    font-weight: 600; font-size: 22px; text-align: center;
  }
  .tagline {
    position: absolute; left: 51px; top: 176px; width: 298px;
    font-weight: 700; font-size: 28px; line-height: 38px; text-align: center;
  }
  .divider {
    position: absolute; left: 51px; top: 278px; width: 298px; height: 2px;
    background: var(--yellow); border-radius: 2px;
  }
  .contact-phone {
    position: absolute; left: 60px; top: 302px;
    display: flex; align-items: center; gap: 14px;
    font-weight: 700; font-size: 35px; color: var(--yellow);
  }
  .contact-web {
    position: absolute; left: 51px; top: 350px; width: 298px; text-align: center;
    font-weight: 700; font-size: 38px; color: var(--yellow);
  }
  .offer-line {
    position: absolute; display: flex; align-items: baseline;
    color: var(--yellow); font-weight: 900;
    text-shadow: 0 4px 8px rgba(0,0,0,0.35);
  }
  .offer-fiber { left: 398px; top: 14px; }
  .offer-data { left: 393px; top: 127px; }
  .offer-number { font-size: 116px; letter-spacing: -4px; line-height: 1.1; }
  .offer-unit { font-size: 42px; font-weight: 700; margin-left: 8px; }
  .offer-calls {
    position: absolute; left: 400px; top: 267px;
    font-weight: 800; font-size: 19.5px; letter-spacing: -0.3px;
    text-shadow: 0 2px 4px rgba(0,0,0,0.5);
  }
  .price {
    position: absolute; left: 400px; top: 296px;
    display: flex; align-items: baseline; gap: 8px;
    text-shadow: 0 4px 10px rgba(0,0,0,0.45);
  }
  .price-label { font-weight: 800; font-size: 22px; }
  .price-amount { font-weight: 900; font-size: 100px; letter-spacing: -5px; line-height: 1.05; }
</style>
</head>
<body>
  <main class="billboard">
    <div class="hero-art" role="img" aria-label="Balón de fútbol volando con estelas de luz azul y amarilla, junto a un móvil con 100 GB en pantalla y un portátil"></div>

    <div class="brand">
      <span class="brand-dot"></span>
      <span class="brand-name">NURA</span>
    </div>
    <p class="services">Wifi | Fibra | Movil | Tv</p>
    <h2 class="tagline">TU FIBRA + MÓVIL<br>AL MEJOR PRECIO</h2>
    <div class="divider"></div>
    <p class="contact-phone">
      <svg width="18" height="32" viewBox="0 0 18 32" aria-hidden="true">
        <rect x="1.5" y="1.5" width="15" height="29" rx="3" fill="none" stroke="#ffffff" stroke-width="2"/>
        <circle cx="9" cy="26" r="1.4" fill="#ffffff"/>
      </svg>
      952 00 0147
    </p>
    <p class="contact-web">www.nu-ra.es</p>

    <h1 class="offer-line offer-fiber"><span class="offer-number">1000</span><span class="offer-unit">Mb</span></h1>
    <p class="offer-line offer-data"><span class="offer-number">+100</span><span class="offer-unit">Gb</span></p>
    <p class="offer-calls">MOVIL CON LLAMADAS ILIMITADAS</p>
    <p class="price"><span class="price-label">por</span><span class="price-amount">18.45€</span></p>
  </main>
</body>
</html>
```